Silver Heron Construction Services

Create a business card for my business consulting company
Danielle Vesk, Founder and CEO
4816 Alder Brook Way, Ste 100
Denver, CO. 80451
303.782.4190 cell
dvesk@silverheronconst.example
www.silverheronconst.example

Target Market(s)

Private Equity and Construction Companies

Industry/Entity Type

Business / Sales Consulting

Contact Information for Business Card

Tag Line that says "Where The Road To Success Is Always Under Construction"

Requirements
Must have
• Logo on both sides of the card.
Nice to have
• Add tagline to the same side of the card as my name and contact info

```html
<!DOCTYPE html>
<html lang="en">
<head>
<meta charset="utf-8">
<title>Silver Heron Construction Services – Business Card</title>
<link rel="stylesheet" href="https://fonts.googleapis.com/css2?family=Montserrat:wght@400;500;700&family=Oswald:wght@500&display=swap">
<style>
  :root {
    --backdrop: #3a3a3a;
    --card-white: #ffffff;
    --card-black: #1c1c1c;
    --ink: #1a1a1a;
    --ink-soft: #333333;
    --divider: #8a8a8a;
    --silver: #a9a9a9;
    --silver-light: #d6d6d6;
  }
  * { box-sizing: border-box; margin: 0; padding: 0; }
  html, body { width: 1200px; height: 1200px; overflow: hidden; }
  body {
    background: var(--backdrop);
    font-family: "Montserrat", sans-serif;
    position: relative;
  }
  .card {
    position: absolute;
    left: 180px;
    width: 840px;
    height: 480px;
    border-radius: 34px;
  }
  .card--front { top: 95px; background: var(--card-white); color: var(--ink); }
  .card--back { top: 625px; background: var(--card-black); color: var(--silver); }

  .brand {
    position: absolute;
    left: 0; right: 0;
    display: flex;
    align-items: center;
    justify-content: center;
    gap: 22px;
    font-family: "Montserrat", sans-serif;
    font-weight: 700;
    text-transform: uppercase;
    letter-spacing: 1px;
    line-height: 1.12;
  }
  .brand__mark { flex: none; border-radius: 50%; background: currentColor; }
  .brand__name { display: block; text-align: left; }
  .card--front .brand { top: 58px; color: var(--ink); font-size: 40px; }
  .card--front .brand__mark { width: 56px; height: 56px; }
  .card--back .brand { top: 110px; color: var(--silver); font-size: 50px; }
  .card--back .brand__mark { width: 72px; height: 72px; }

  .holder {
    position: absolute;
    left: 60px;
    bottom: 62px;
  }
  .holder__name { font-size: 32px; font-weight: 500; letter-spacing: 1px; text-transform: uppercase; }
  .holder__title { font-size: 18px; font-weight: 400; letter-spacing: 1px; text-transform: uppercase; color: var(--ink-soft); margin-top: 4px; }

  .divider {
    position: absolute;
    left: 390px;
    top: 240px;
    width: 1px;
    height: 180px;
    background: var(--divider);
  }
  .contact {
    position: absolute;
    left: 420px;
    top: 250px;
    list-style: none;
    font-size: 20px;
    line-height: 1.3;
    color: var(--ink-soft);
  }
  .contact li { display: flex; align-items: flex-start; gap: 10px; margin-bottom: 6px; }
  .contact svg { flex: none; width: 20px; height: 22px; margin-top: 2px; fill: var(--ink); }

  .tagline {
    position: absolute;
    left: 0; right: 0;
    bottom: 58px;
    text-align: center;
    font-family: "Oswald", sans-serif;
    font-weight: 500;
    font-size: 34px;
    letter-spacing: 1px;
    text-transform: uppercase;
    color: var(--silver-light);
  }
</style>
</head>
<body>
  <section class="card card--front" aria-label="Business card front">
    <div class="brand"><span class="brand__mark"></span><span class="brand__name">Silver Heron<br>Construction Services</span></div>
    <div class="holder">
      <p class="holder__name">Danielle Vesk</p>
      <p class="holder__title">Founder and CEO</p>
    </div>
    <div class="divider"></div>
    <ul class="contact">
      <li>
        <svg viewBox="0 0 18 20"><path d="M4 1h10a2 2 0 0 1 2 2v14a2 2 0 0 1-2 2H4a2 2 0 0 1-2-2V3a2 2 0 0 1 2-2zm0 2v12h10V3zm5 13a1 1 0 1 0 0 2 1 1 0 0 0 0-2z"/></svg>
        <span>303.782.4190</span>
      </li>
      <li>
        <svg viewBox="0 0 18 20"><path d="M1 5h16v11H1zm1.5 1.2L9 11l6.5-4.8V6.2H2.5z"/></svg>
        <span>dvesk@silverheronconst.example</span>
      </li>
      <li>
        <svg viewBox="0 0 18 20"><path d="M9 1a6 6 0 0 1 6 6c0 4.5-6 12-6 12S3 11.5 3 7a6 6 0 0 1 6-6zm0 3.5A2.5 2.5 0 1 0 9 9.5 2.5 2.5 0 0 0 9 4.5z"/></svg>
        <span>4816 Alder Brook Way, Ste 100<br>Denver, CO. 80451</span>
      </li>
    </ul>
  </section>

  <section class="card card--back" aria-label="Business card back">
    <div class="brand"><span class="brand__mark"></span><span class="brand__name">Silver Heron<br>Construction Services</span></div>
    <p class="tagline">The road to success is always under construction</p>
  </section>
</body>
</html>
```